Lanternfield Systems Bi Fold Brocher

I need a bi fold (front/back page 1 & front/back page 2) color brochure designed to pass out to clients at a convention. My website is lanternfieldsys.example. Please take images and text from the website to create the brochure. Use the products and product descriptions to display what we offer. Use the text and quotes to describe what we do. Make it professional, descriptive, and full of useful information.

Industry/Entity Type

Business Software

Font styles to use
Serif

Colors
00a990
33b8a4
86cfc6
fbf289
0255a3
3377b5
85acd3

Requirements
Must have
• Contact Info:
• Address:
• 728 Mossgate Boulevard
• Building 200, Suite 1187
• Cumming, GA 30987
• Telephone: 1 (555) 274.8816
• Toll Free: 1 (800) 555.0147
• Email: contact@lanternfieldsys.example
Nice to have
• Good backrounds

```html
<!DOCTYPE html>
<html lang="en">
<head>
<meta charset="utf-8">
<title>Lanternfield Systems Bi-Fold Brochure</title>
<link href="https://fonts.googleapis.com/css2?family=Arimo:wght@400;700&display=swap" rel="stylesheet">
<style>
:root{
  --navy:#1b3f6b;
  --blue:#1f5f96;
  --blue-light:#3377b5;
  --teal:#13807a;
  --teal-bright:#33b8a4;
  --teal-soft:#86cfc6;
  --cyan-wash:#e0f2f3;
  --ink:#2b2b2b;
  --paper:#ffffff;
  --stage:#e6e9ec;
}
*{box-sizing:border-box;margin:0;padding:0}
html,body{width:1200px;height:969px;overflow:hidden}
body{background:var(--stage);font-family:"Arimo",Arial,sans-serif;color:var(--ink);position:relative}
.spread{position:absolute;background:var(--paper);box-shadow:0 6px 18px rgba(0,0,0,.25);overflow:hidden}
.abs{position:absolute}

/* outer spread */
.outer{left:40px;top:50px;width:740px;height:490px;z-index:2}
.outer .top-band{left:0;top:0;width:740px;height:115px;background:var(--navy)}
.outer .back-title-band{left:0;top:115px;width:270px;height:40px;background:var(--navy)}
.back-title{left:40px;top:62px;color:#fff;font-size:26px;line-height:1.05;font-weight:400}
.brand-front{right:40px;top:38px;display:flex;align-items:center;gap:10px;color:#fff;font-weight:700;font-size:30px}
.brand-dot{width:22px;height:22px;border-radius:50%;background:var(--teal-bright);flex:none}
.hero-photo{left:270px;top:115px;width:470px;height:190px;background:linear-gradient(120deg,#3f8fa6 0%,#8d9aa3 40%,#6b4a3c 70%,#b9c1c6 100%)}
.faded-photo{left:0;top:155px;width:270px;height:165px;background:linear-gradient(180deg,#f4f6f7,#dfe6ea)}
.checklist{left:40px;top:165px;list-style:none;font-size:10.5px;line-height:15.5px;color:#1c2a38}
.checklist li::before{content:"\2713";color:var(--teal-bright);font-weight:700;margin-right:5px}
.url-band-right{left:270px;top:290px;width:470px;height:30px;background:var(--blue-light)}
.url-band{left:0;top:320px;width:740px;height:48px;background:var(--blue)}
.url{color:#fff;font-weight:700;font-size:13px;display:flex;align-items:center;gap:5px}
.url::before{content:">";display:inline-flex;align-items:center;justify-content:center;width:13px;height:13px;border-radius:50%;background:var(--teal-bright);font-size:9px}
.url-back{left:40px;top:337px}
.url-front{right:30px;top:297px}
.front-title-box{left:430px;top:345px;width:310px;height:145px;background:var(--teal)}
.front-title{left:470px;top:375px;color:#fff;font-weight:700;font-size:30px;line-height:1.1}
.brand-back{left:30px;top:414px;display:flex;align-items:center;gap:7px;color:var(--navy);font-weight:700;font-size:16px;white-space:nowrap}
.brand-back .brand-dot{width:14px;height:14px}
.contact{left:240px;top:392px;font-size:8.5px;line-height:12px;color:var(--navy);font-style:normal;white-space:nowrap}
.contact h3{font-size:12px;margin-bottom:3px}

/* inner spread */
.inner{left:430px;top:430px;width:710px;height:500px;z-index:1}
.intro{left:22px;top:98px;width:320px;font-size:8.5px;line-height:12px;list-style:none}
.intro li.tick::before{content:"\2713";margin-right:4px}
.clients{left:22px;top:182px;display:flex;gap:12px}
.clients span{width:42px;height:20px;border-radius:3px;background:#c9cdd1}
.overview-wash{left:0;top:230px;width:355px;height:110px;background:linear-gradient(90deg,#fff 20%,#dde9f4 100%)}
.overview-title{left:22px;top:247px;font-size:26px;color:var(--navy);font-weight:700;white-space:nowrap}
.overview-title span{font-weight:400}
.computer{left:252px;top:210px;width:90px;height:112px;background:linear-gradient(180deg,#e9eef2,#b9c4cc);border-radius:4px}
.web-bar{left:210px;top:330px;width:145px;height:30px;background:var(--navy);color:#fff;font-size:12px;font-weight:700;display:flex;align-items:center;justify-content:center}
.features-table{left:22px;top:300px;width:178px;border:1px solid #9aa6b1;font-size:7.5px;line-height:11px}
.features-table p{padding:6px 7px;border-bottom:1px solid #9aa6b1}
.features-table p:last-child{border-bottom:0}
.tech-title{left:235px;top:372px;font-size:12px;font-weight:700;color:var(--navy)}
.tech-grid{left:222px;top:395px;width:120px;display:grid;grid-template-columns:repeat(2,40px);gap:8px 24px}
.tech-grid span{width:36px;height:20px;border-radius:50%;background:#d4d9dd}

.right-panel{left:355px;top:0;width:355px;height:500px;border-left:1px solid #cfd5da}
.sf-title{left:10px;top:22px;font-size:29px;font-weight:700;color:var(--navy)}
.sf-title span{font-weight:400;color:var(--teal-bright)}
.sf-intro{left:12px;top:62px;width:155px;font-size:8.5px;line-height:11.5px}
.tablets{left:38px;top:135px;width:120px;height:85px;background:linear-gradient(180deg,#2a2f35,#4b7da6)}
.devices{left:170px;top:90px;width:180px;height:135px;background:linear-gradient(180deg,#2c3238,#58677a)}
.arrow{left:0;top:210px;width:200px;height:40px}
.arrow-text{left:18px;top:218px;font-size:10px;line-height:11px;color:#1d3550}
.wash-band{left:0;top:250px;width:355px;height:188px;background:var(--cyan-wash)}
.photo{top:262px;width:104px;height:76px}
.p1{left:14px;background:linear-gradient(135deg,#5a6068,#a9b0b5)}
.p2{left:126px;background:linear-gradient(135deg,#3a4a5c,#c4a34a)}
.p3{left:238px;background:linear-gradient(135deg,#c9ced3,#5c6670)}
.caption{top:344px;width:104px;font-size:6.8px;line-height:8.6px}
.c1{left:14px}.c2{left:126px}.c3{left:238px}
.edi{left:22px;top:452px;width:230px;font-size:9.5px;line-height:12px;color:var(--navy)}
.edi-illustration{left:268px;top:442px;width:75px;height:52px;background:linear-gradient(135deg,#8fd0e8,#f3c35a);border-radius:6px}
</style>
</head>
<body>

<section class="spread outer" aria-label="Brochure outer spread">
  <div class="abs top-band"></div>
  <div class="abs back-title-band"></div>
  <h2 class="abs back-title">Cost Savings &amp;<br>Efficiencies</h2>
  <div class="abs brand-front"><span class="brand-dot"></span>Lanternfield Systems</div>
  <div class="abs faded-photo" role="img" aria-label="Faded rail yard photograph behind the checklist"></div>
  <ul class="abs checklist">
    <li>Improved Yard Control</li>
    <li>Corporate Analytics and Dashboards</li>
    <li>Railcar Inspections</li>
    <li>Maintain Railcar Statuses</li>
    <li>Reduction in Human Error</li>
    <li>Demurrage Management</li>
    <li>Customer Portals</li>
    <li>Functionality</li>
    <li>Organization</li>
    <li>Automation</li>
  </ul>
  <div class="abs hero-photo" role="img" aria-label="Photograph of a locomotive and freight railcars in a rail terminal"></div>
  <div class="abs url-band-right"></div>
  <div class="abs url url-front">lanternfieldsys.example</div>
  <div class="abs url-band"></div>
  <div class="abs url url-back">lanternfieldsys.example</div>
  <div class="abs front-title-box"></div>
  <h1 class="abs front-title">Rail terminal<br>management<br>Software</h1>
  <div class="abs brand-back"><span class="brand-dot"></span>Lanternfield Systems</div>
  <address class="abs contact">
    <h3>Contact Info:</h3>
    728 Mossgate Boulevard<br>
    Building 200, Suite 1187<br>
    Cumming, GA 30987<br>
    Telephone: 1 (555) 274.8816<br>
    Toll Free: 1 (800) 555.0147<br>
    Email: contact@lanternfieldsys.example
  </address>
</section>

<section class="spread inner" aria-label="Brochure inner spread">
  <ul class="abs intro">
    <li>&nbsp;&nbsp;&nbsp;understands the cost of the software upfront.</li>
    <li class="tick">Grow our client base while never loosing the commitment to providing quick, honest answers, and cost effective solutions.</li>
    <li class="tick">Our current clients will attest to and our future clients will unquestionably receive the most user-friendly and robust software solutions available to manage their rail terminals.</li>
  </ul>
  <div class="abs clients" aria-label="Client badges"><span></span><span></span><span></span><span></span><span></span><span></span></div>

  <div class="abs overview-wash"></div>
  <h2 class="abs overview-title">Product <span>Overview</span></h2>
  <div class="abs computer" role="img" aria-label="Illustration of a desktop computer with wireless signal"></div>
  <div class="abs web-bar">Web-Based Application</div>
  <div class="abs features-table">
    <p>Easily operated and strait forward dashboard with drop down menus for uncomplicated management of your rail terminal.</p>
    <p>Detailed inspection component with current and state of the art easy to use technology.</p>
    <p>Compelling transloading software. Mobile Data Collection, ERP Integration, Custom Ad-Hoc Reporting, Transload Customer Portal, and Scale House Integration.</p>
    <p>Comprehensive and accurate corporate reporting</p>
  </div>
  <div class="abs tech-title">Technology</div>
  <div class="abs tech-grid" aria-label="Technology badges"><span></span><span></span><span></span><span></span><span></span><span></span></div>

  <div class="abs right-panel">
    <h2 class="abs sf-title">Software <span>Features</span></h2>
    <p class="abs sf-intro">Know where every rail car is all the time. Managing rail car locations within your terminal becomes simple and fast using our web-based or tablet application.</p>
    <div class="abs tablets" role="img" aria-label="Two handheld tablets showing the inspection app"></div>
    <div class="abs devices" role="img" aria-label="Desktop monitor and tablet showing the yard dashboard"></div>
    <svg class="abs arrow" viewBox="0 0 200 40" aria-hidden="true"><polygon points="0,4 165,4 165,0 200,20 165,40 165,36 0,36" fill="#86cfc6"/></svg>
    <div class="abs arrow-text">Mobile Inspections -<br>Accurate and Paperless...</div>
    <div class="abs wash-band"></div>
    <div class="abs photo p1" role="img" aria-label="Photograph of a locomotive at a transload facility"></div>
    <div class="abs photo p2" role="img" aria-label="Photograph of a worker inspecting a railcar"></div>
    <div class="abs photo p3" role="img" aria-label="Photograph of tank cars lined up in a yard"></div>
    <p class="abs caption c1">Manage rail transloading activities to and from a truck or vessel. The software allows the transload terminal operation to effectively and efficiently manage each transaction, decrease paper processing, and provide customers with live inventory and access to transactions.</p>
    <p class="abs caption c2">Automated railcar inspections are now affordable and reliable. You can create unlimited inspection forms and assign specific inspections to individual users. No more paper, no more going back for photos, and no more sorting through the daily inspection sheets.</p>
    <p class="abs caption c3">Built-in demurrage management functionality that maintains key data to track and respond to demurrage challenges.</p>
    <p class="abs edi">Lanternfield Systems has built a robust system for handling and generating EDI messages in order to automate data entry and communicate key pieces of data with the carrier.</p>
    <div class="abs edi-illustration" role="img" aria-label="Illustration of freight transport by plane, truck and map"></div>
  </div>
</section>

</body>
</html>
```